Larkfield Financial Plans

I am looking for a complete resdesign of my small financial presentation. This is a Word Doc/PDF that I print off when meeting with people in private. I often present my "two pager" that I have been using for years and years. It tells them the basics of what I do, how I help people and foundational financial principles.

I have recently gone out on my own in business and have completely rebranded. This presentation is my most used tool, so it is the first of many things I would like to redo. I am hoping it will somehow coordinate with the colors of my business, not necessarily the EXACT same 3 colors everywhere, but have the design colors compliment.

I've uploaded all my logo designs, as well as the current "two-pager". I am not against it going to 3 pages if needed. As it will still land on 2 pages with duplex printing.

It has always been VERY simple. I am wanting it built into a more professional and design specific format, to show off my branding, without being over cluttered.

I am completely open to ANY graphics changes. Obviously some are very novice, the house on the last page has always been overly simplified.

```html
<!DOCTYPE html>
<html lang="en">
<head>
<meta charset="utf-8">
<title>Larkfield – Deck Idea 2 – Landscape</title>
<link href="https://fonts.googleapis.com/css2?family=Barlow:wght@400;500;600;700&display=swap" rel="stylesheet">
<style>
  :root {
    --brand-green: #00a63e;
    --brand-navy: #0e1b2f;
    --ink: #161c2a;
    --paper: #ffffff;
    --icon-ring: #d8efe0;
    --sky-deep: #1a2b36;
    --sky-teal: #4f7f8a;
    --sunset: #e08a3a;
    --water: #2a3740;
  }
  * { box-sizing: border-box; margin: 0; padding: 0; }
  html, body { width: 1200px; height: 848px; overflow: hidden; background: var(--paper); }
  body { position: relative; font-family: "Barlow", Arial, sans-serif; color: var(--ink); }

  .sheet-title { position: absolute; left: 57px; top: 56px; font-size: 16px; font-weight: 500; }
  .annotation { position: absolute; font-size: 12.5px; line-height: 20px; font-weight: 500; }
  .annotation--intro { left: 57px; top: 152px; }
  .annotation--alt { left: 651px; top: 152px; }
  .annotation--note { left: 82px; top: 621px; font-size: 10px; line-height: 15px; }

  .slide { position: absolute; top: 210px; width: 531px; height: 377px; overflow: hidden; border: 1px solid #1a3a28; }
  .slide--green { left: 42px; background: var(--brand-green); }
  .slide--photo { left: 617px; }
  .slide__photo {
    position: absolute; inset: 0 0 49px 0;
    background:
      radial-gradient(ellipse 45% 22% at 48% 40%, rgba(240,150,60,.85), rgba(224,138,58,0) 70%),
      linear-gradient(180deg, var(--sky-deep) 0%, var(--sky-teal) 22%, #6b8f95 35%, #b87a4a 42%, var(--water) 55%, #1c262d 100%);
  }

  .wordmark {
    position: absolute; left: 53px; top: 53px; width: 133px; height: 42px;
    background: var(--brand-navy); color: var(--paper);
    display: flex; flex-direction: column; align-items: center; justify-content: center;
    font-weight: 600; letter-spacing: .5px; line-height: 1;
  }
  .wordmark__name { font-size: 17px; }
  .wordmark__sub { font-size: 6.5px; letter-spacing: 1.2px; margin-top: 4px; }

  .intro { position: absolute; left: 53px; top: 141px; color: var(--paper); font-weight: 500; }
  .intro p { margin-bottom: 16px; }
  .slide--green .intro { font-size: 11px; line-height: 15.5px; }
  .slide--photo .intro { font-size: 12.5px; line-height: 17px; top: 141px; }
  .slide--photo .intro p { margin-bottom: 16px; }

  .areas { position: absolute; left: 358px; top: 141px; width: 160px; }
  .areas__lead { font-size: 6.5px; line-height: 9px; font-weight: 700; color: var(--paper); margin-bottom: 13px; }
  .areas__list { list-style: none; }
  .areas__item { display: flex; align-items: center; height: 23.5px; font-size: 6.5px; font-weight: 700; }
  .slide--green .areas__item { color: var(--ink); }
  .slide--photo .areas__item { color: var(--paper); }
  .areas__icon { width: 18px; height: 18px; margin-right: 9px; flex: none; }

  .slide__footer { position: absolute; left: 0; right: 0; bottom: 0; height: 49px; display: flex; align-items: center; padding-left: 53px; color: var(--paper); font-size: 11.5px; font-weight: 600; }
  .slide--green .slide__footer { background: var(--brand-navy); }
  .slide--photo .slide__footer { background: var(--brand-green); }
</style>
</head>
<body>
  <h1 class="sheet-title">Larkfield – Deck Idea 2 - LANDSCAPE</h1>
  <p class="annotation annotation--intro">First page is again an introduction<br>Less information to pace the presentation.</p>
  <p class="annotation annotation--alt">Again alternative with the starry night inspiring photo.</p>

  <svg width="0" height="0" style="position:absolute" aria-hidden="true">
    <defs>
      <g id="ring"><circle cx="9" cy="9" r="8.3" fill="#e9f6ee" stroke="#ffffff" stroke-width="1.2"/></g>
      <symbol id="i-cash" viewBox="0 0 18 18"><use href="#ring"/><circle cx="9" cy="9" r="3.6" fill="none" stroke="#1c8a47" stroke-width="1.3"/></symbol>
      <symbol id="i-umbrella" viewBox="0 0 18 18"><use href="#ring"/><path d="M4.5 9a4.5 4.5 0 0 1 9 0z" fill="#1c8a47"/><path d="M9 9v3.5a1 1 0 0 1-2 0" fill="none" stroke="#1c8a47" stroke-width="1"/></symbol>
      <symbol id="i-debt" viewBox="0 0 18 18"><use href="#ring"/><rect x="5" y="6" width="8" height="6" rx="1" fill="none" stroke="#1c8a47" stroke-width="1.1"/><path d="M5 8h8" stroke="#1c8a47" stroke-width="1"/></symbol>
      <symbol id="i-fund" viewBox="0 0 18 18"><use href="#ring"/><rect x="4.5" y="6.5" width="9" height="5" rx="1" fill="#1c8a47"/><circle cx="9" cy="9" r="1.3" fill="#e9f6ee"/></symbol>
      <symbol id="i-build" viewBox="0 0 18 18"><use href="#ring"/><path d="M5 12.5l3-3 2 2 3-4" fill="none" stroke="#1c8a47" stroke-width="1.3"/></symbol>
      <symbol id="i-preserve" viewBox="0 0 18 18"><use href="#ring"/><rect x="5.5" y="5.5" width="7" height="7" rx="1" fill="#1c8a47"/></symbol>
    </defs>
  </svg>

  <section class="slide slide--green">
    <div class="wordmark"><span class="wordmark__name">LARKFIELD</span><span class="wordmark__sub">FINANCIAL PLANS</span></div>
    <div class="intro">
      <p>Independent financial solutions<br>tailored to your needs.</p>
      <p>Experienced financial advisor providing<br>rock-solid recommendations,<br>trustworthy advice and complete services.</p>
      <p>Together, we can plan for all of life's events,<br>even the unexpected.</p>
    </div>
    <div class="areas">
      <p class="areas__lead">Helping average ordinary people navigate<br>their wealth in the following areas:</p>
      <ul class="areas__list">
        <li class="areas__item"><svg class="areas__icon"><use href="#i-cash"/></svg>Cash flow</li>
        <li class="areas__item"><svg class="areas__icon"><use href="#i-umbrella"/></svg>Income protection</li>
        <li class="areas__item"><svg class="areas__icon"><use href="#i-debt"/></svg>Debt management</li>
        <li class="areas__item"><svg class="areas__icon"><use href="#i-fund"/></svg>Emergency fund</li>
        <li class="areas__item"><svg class="areas__icon"><use href="#i-build"/></svg>Build wealth</li>
        <li class="areas__item"><svg class="areas__icon"><use href="#i-preserve"/></svg>Preserve wealth</li>
      </ul>
    </div>
    <footer class="slide__footer">www.larkfieldplans.ca</footer>
  </section>

  <section class="slide slide--photo">
    <div class="slide__photo" role="img" aria-label="Photo of a starry night sky over a calm lake with a sunset glowing on the horizon and a small tree-covered island"></div>
    <div class="wordmark"><span class="wordmark__name">LARKFIELD</span><span class="wordmark__sub">FINANCIAL PLANS</span></div>
    <div class="intro">
      <p>Independent financial solutions<br>tailored to your needs.</p>
      <p>Experienced financial advisor<br>providing rock-solid recommendations,<br>trustworthy advice and complete services.</p>
      <p>Together, we can plan for all of life's events,<br>even the unexpected.</p>
    </div>
    <div class="areas">
      <p class="areas__lead">Helping average ordinary people navigate<br>their wealth in the following areas:</p>
      <ul class="areas__list">
        <li class="areas__item"><svg class="areas__icon"><use href="#i-cash"/></svg>Cash flow</li>
        <li class="areas__item"><svg class="areas__icon"><use href="#i-umbrella"/></svg>Income protection</li>
        <li class="areas__item"><svg class="areas__icon"><use href="#i-debt"/></svg>Debt management</li>
        <li class="areas__item"><svg class="areas__icon"><use href="#i-fund"/></svg>Emergency fund</li>
        <li class="areas__item"><svg class="areas__icon"><use href="#i-build"/></svg>Build wealth</li>
        <li class="areas__item"><svg class="areas__icon"><use href="#i-preserve"/></svg>Preserve wealth</li>
      </ul>
    </div>
    <footer class="slide__footer">www.larkfieldplans.ca</footer>
  </section>

  <p class="annotation annotation--note">Note - the following pages would<br>follow the layout grid but include<br>more details.</p>
</body>
</html>
```